Retail Jewelry Business Card Design Project

We are in need of a new business card design for a retail jewelry store. This store is in the business of fine jewelry including but not specific to bridal jewelry, diamonds, designer jewelry and watches.

This store has been in business for 20 years but continues to strive for a modern professional appeal. The main colors use for this business are a royal blue, white and silver.

Target Market(s)

Target market is ages 18-50

Industry/Entity Type

Jewelry

Requirements
Must have
• Sales Person Name
Sales Person Email Address

Store Address
Store Phone
Website

Standard business card size. No odd shapes or sizes.
Nice to have
• Overall modern feel for card.

We have thought that a design with a nice feature of the logo on the back of the card would be nice but open to ideas.
Should not have
• No specific images of jewelry should be used.

```html
<!DOCTYPE html>
<html lang="en">
<head>
<meta charset="utf-8">
<title>Morgan Hale Fine Jewelry – Business Card</title>
<link rel="stylesheet" href="https://fonts.googleapis.com/css2?family=Arimo:wght@400&family=Libre+Baskerville:wght@700&display=swap">
<style>
  :root {
    --stage: #3b3b3d;
    --card-center: #ffffff;
    --card-edge: #d9d6e3;
    --royal: #2b2a8f;
    --royal-faint: rgba(120, 112, 160, 0.10);
    --shadow: rgba(0, 0, 0, 0.45);
  }
  * { margin: 0; padding: 0; box-sizing: border-box; }
  html, body {
    width: 1200px;
    height: 1000px;
    overflow: hidden;
    background: var(--stage);
  }
  .canvas {
    width: 1200px;
    height: 1000px;
    display: flex;
    flex-direction: column;
    align-items: center;
    justify-content: center;
    gap: 56px;
  }
  .card {
    position: relative;
    width: 700px;
    height: 400px;
    overflow: hidden;
    background: radial-gradient(ellipse at 55% 50%, var(--card-center) 35%, var(--card-edge) 100%);
    box-shadow: 0 14px 30px var(--shadow);
  }
  .brand-name {
    font-family: "Libre Baskerville", serif;
    font-weight: 700;
    color: var(--royal);
    line-height: 1.15;
    text-align: center;
  }

  /* Back: contact details */
  .card-back .contact {
    position: absolute;
    left: 58px;
    top: 62px;
    font-family: "Arimo", sans-serif;
    font-size: 17px;
    line-height: 30px;
    color: var(--royal);
    list-style: none;
  }
  .card-back .contact .spacer { height: 22px; }
  .card-back .brand-name {
    position: absolute;
    right: 48px;
    bottom: 56px;
    font-size: 24px;
  }

  /* Front: brand */
  .card-front .brand-backdrop {
    position: absolute;
    left: 0;
    right: 0;
    top: 96px;
    font-size: 92px;
    color: var(--royal-faint);
  }
  .card-front .brand-name.primary {
    position: absolute;
    left: 0;
    right: 0;
    top: 138px;
    font-size: 50px;
  }
</style>
</head>
<body>
  <main class="canvas">
    <section class="card card-back" aria-label="Card back with contact details">
      <ul class="contact">
        <li class="person">Morgan Hale Prescott</li>
        <li class="email">morgan@morganhalejewelry.com</li>
        <li class="phone">0437 512 960</li>
        <li class="spacer" aria-hidden="true"></li>
        <li class="street">2218 Jefferson Avenue</li>
        <li class="city">Harbor Springs, FL 32499</li>
        <li class="web">www.morganhalejewelry.com</li>
      </ul>
      <p class="brand-name">Morgan Hale<br>Fine Jewelry</p>
    </section>

    <section class="card card-front" aria-label="Card front with store name">
      <p class="brand-name brand-backdrop" aria-hidden="true">Morgan Hale</p>
      <p class="brand-name primary">Morgan Hale<br>Fine Jewelry</p>
    </section>
  </main>
</body>
</html>
```